I'm a magician . hypnotist also a good barber. I need this all to be shown in good detail on the cards.

Magician

Magician/ hypnotist/barber Morris quill. One of the best. Tel 07412 638204
Email.Velvetowl27@postmail-example.net
Title of card velvet owl.

```html
<!DOCTYPE html>
<html lang="en">
<head>
<meta charset="utf-8">
<title>Morris quill – Magician, Hypnotist, Barber</title>
<link rel="stylesheet" href="https://fonts.googleapis.com/css2?family=Cantarell:wght@400;700&display=swap">
<style>
  :root {
    --frame: #000000;
    --curtain-top: #a8302c;
    --curtain-mid: #d9675f;
    --curtain-low: #c4524c;
    --stage-edge: #3b1c12;
    --stage-floor: #7a4a30;
    --ink: #111111;
    --tile: #ffffff;
    --icon: #2b2b2b;
    --glow: rgba(0,0,0,0.55);
  }
  html, body {
    margin: 0;
    padding: 0;
    width: 1200px;
    height: 791px;
    overflow: hidden;
    background: #ffffff;
  }
  .card {
    position: relative;
    width: 1200px;
    height: 791px;
    box-sizing: border-box;
    border: 14px solid var(--frame);
    overflow: hidden;
    font-family: "Cantarell", "Trebuchet MS", sans-serif;
    color: var(--ink);
  }
  .stage-backdrop {
    position: absolute;
    inset: 0;
    background:
      linear-gradient(180deg,
        var(--curtain-top) 0%,
        var(--curtain-low) 14%,
        var(--curtain-mid) 45%,
        var(--curtain-low) 84%,
        var(--stage-edge) 88%,
        var(--stage-floor) 93%,
        var(--stage-edge) 100%);
  }
  .headline {
    position: absolute;
    left: 0;
    width: 1172px;
    text-align: center;
    margin: 0;
  }
  .name {
    top: 126px;
    font-size: 68px;
    font-weight: 700;
    transform: translateX(-6px);
  }
  .tagline {
    top: 202px;
    font-size: 46px;
    font-weight: 700;
    transform: translateX(-6px);
  }
  .service {
    position: absolute;
    top: 272px;
    display: flex;
    flex-direction: column;
    align-items: center;
  }
  .service-tile {
    background: var(--tile);
    border: 7px solid var(--frame);
    border-radius: 8px;
    box-sizing: border-box;
    height: 168px;
    display: flex;
    align-items: center;
    justify-content: center;
  }
  .service-label {
    margin-top: 16px;
    font-size: 60px;
    font-weight: 700;
    text-shadow: 0 0 10px var(--glow), 0 0 4px var(--glow);
    letter-spacing: 0.5px;
  }
  .service--magic { left: 130px; width: 170px; }
  .service--magic .service-tile { width: 168px; }
  .service--hypno { left: 448px; width: 304px; }
  .service--hypno .service-tile { width: 262px; }
  .service--barber { left: 812px; width: 200px; }
  .service--barber .service-tile { width: 173px; border-radius: 4px; }
  .contact {
    position: absolute;
    left: 0;
    width: 1172px;
    text-align: center;
    font-size: 37px;
    font-weight: 700;
    line-height: 46px;
    top: 592px;
    transform: translateX(-16px);
  }
  .contact p { margin: 0; }
</style>
</head>
<body>
  <main class="card">
    <div class="stage-backdrop" role="img" aria-label="Theatre stage with draped red curtains and a wooden stage floor"></div>

    <h1 class="headline name">Morris quill</h1>
    <p class="headline tagline">One of the best</p>

    <section class="service service--magic">
      <div class="service-tile">
        <svg width="120" height="120" viewBox="0 0 100 100" aria-hidden="true">
          <polygon fill="var(--icon)" points="50,4 61,38 97,38 68,59 79,94 50,73 21,94 32,59 3,38 39,38"/>
        </svg>
      </div>
      <span class="service-label">Magician</span>
    </section>

    <section class="service service--hypno">
      <div class="service-tile">
        <svg width="230" height="120" viewBox="0 0 230 120" aria-hidden="true">
          <path fill="var(--icon)" d="M5 60 Q115 -20 225 60 Q115 140 5 60 Z"/>
          <circle cx="115" cy="60" r="38" fill="var(--tile)"/>
          <path fill="none" stroke="var(--icon)" stroke-width="4" stroke-linecap="round"
            d="M115 60 m0 -4 a4 4 0 1 1 -4 4 a8 8 0 0 1 8 -8 a12 12 0 0 1 12 12 a16 16 0 0 1 -16 16 a20 20 0 0 1 -20 -20 a24 24 0 0 1 24 -24 a28 28 0 0 1 28 28"/>
        </svg>
      </div>
      <span class="service-label">Hypnotist</span>
    </section>

    <section class="service service--barber">
      <div class="service-tile">
        <svg width="140" height="140" viewBox="0 0 140 140" aria-hidden="true">
          <g fill="var(--icon)">
            <rect x="22" y="10" width="14" height="118" rx="2"/>
            <rect x="36" y="14" width="14" height="3"/>
            <rect x="36" y="21" width="14" height="3"/>
            <rect x="36" y="28" width="14" height="3"/>
            <rect x="36" y="35" width="14" height="3"/>
            <rect x="36" y="42" width="14" height="3"/>
            <rect x="36" y="49" width="14" height="3"/>
            <rect x="36" y="56" width="14" height="3"/>
            <rect x="36" y="63" width="14" height="3"/>
            <rect x="36" y="70" width="14" height="3"/>
            <rect x="36" y="77" width="14" height="3"/>
            <rect x="36" y="84" width="14" height="3"/>
            <rect x="36" y="91" width="14" height="3"/>
            <rect x="36" y="98" width="14" height="3"/>
            <rect x="36" y="105" width="14" height="3"/>
            <rect x="36" y="112" width="14" height="3"/>
            <rect x="36" y="119" width="14" height="3"/>
          </g>
          <g fill="none" stroke="var(--icon)" stroke-width="5" stroke-linecap="round">
            <line x1="82" y1="18" x2="100" y2="96"/>
            <line x1="118" y1="18" x2="94" y2="96"/>
            <circle cx="86" cy="112" r="12"/>
            <circle cx="114" cy="112" r="12"/>
          </g>
          <circle cx="97" cy="80" r="3" fill="var(--icon)"/>
        </svg>
      </div>
      <span class="service-label">Barber</span>
    </section>

    <address class="contact" style="font-style: normal;">
      <p>Tel 07412 638204</p>
      <p>Email.Velvetowl27@postmail-example.net</p>
    </address>
  </main>
</body>
</html>
```